Technology Consulting
I need single sided standard sized Business Card [3.5" x 2"]
use something that looks conservative and contemporary
Simple
Mark Delaney
System's Engineer
48 Harrow Lane
mdelaney@quorvalenconsulting.com
http://www.quorvalenconsutling.com
use a font that looks conservative and contemporary

```html
<!DOCTYPE html>
<html lang="en">
<head>
<meta charset="utf-8">
<title>Quorvalen Consulting Stationery</title>
<link rel="stylesheet" href="https://fonts.googleapis.com/css2?family=Open+Sans:wght@400;600;700;800&display=swap">
<style>
  :root {
    --bg: #e9e9e9;
    --paper: #ffffff;
    --brand: #1f4f99;
    --brand-dark: #0e2a5c;
    --brand-light: #4d7fc6;
    --ink: #333a44;
    --muted: #8a9099;
    --rule: #b9bec6;
    --ghost: #f1f2f4;
  }
  * { box-sizing: border-box; margin: 0; padding: 0; }
  html, body { width: 1200px; height: 562px; overflow: hidden; }
  body { background: var(--bg); font-family: "Open Sans", Arial, sans-serif; color: var(--ink); position: relative; }

  .item-label { position: absolute; font-size: 7px; font-weight: 600; color: #555; text-align: center; }
  .sheet { position: absolute; background: var(--paper); box-shadow: 0 1px 4px rgba(0,0,0,.25); overflow: hidden; }

  .brand { display: flex; align-items: center; gap: 5px; }
  .brand-dot { width: 18px; height: 18px; border-radius: 50%; background: var(--brand); flex: none; }
  .brand-name { font-weight: 800; color: var(--brand); font-size: 13px; letter-spacing: .5px; line-height: 1; }

  .contact { font-size: 4px; line-height: 6px; color: var(--muted); }

  .ghost-circle { position: absolute; border-radius: 50%; background: var(--ghost); }
  .footer-band { position: absolute; left: 0; right: 0; bottom: 0; height: 7px;
    background: linear-gradient(90deg, var(--brand-dark), var(--brand) 70%, var(--brand-light)); }

  /* Fax */
  .fax { left: 19px; top: 29px; width: 281px; height: 512px; }
  .fax .brand { position: absolute; left: 16px; top: 16px; }
  .fax .contact { position: absolute; left: 196px; top: 14px; }
  .fax-title { position: absolute; right: 18px; top: 54px; font-size: 6px; font-weight: 700; }
  .fax-table { position: absolute; left: 16px; top: 62px; width: 248px; border-collapse: collapse; font-size: 4.5px; }
  .fax-table td { border: .6px solid var(--rule); height: 11px; padding-left: 3px; }
  .fax-options { position: absolute; left: 16px; top: 130px; width: 248px; display: flex; justify-content: space-between; font-size: 4px; }
  .fax-options span::before { content: ""; display: inline-block; width: 4px; height: 4px; border: .6px solid var(--muted); margin-right: 3px; vertical-align: -1px; }
  .fax-divider { position: absolute; left: 16px; right: 16px; top: 142px; border-top: .6px solid var(--rule); }

  /* Letterhead */
  .letterhead { left: 408px; top: 29px; width: 288px; height: 512px; }
  .letterhead .brand { position: absolute; left: 16px; top: 16px; }
  .letterhead .contact { position: absolute; left: 200px; top: 14px; }

  /* Cards */
  .card { position: absolute; width: 156px; height: 86px; border-radius: 2px; overflow: hidden; box-shadow: 0 1px 4px rgba(0,0,0,.25); }
  .card-front { left: 780px; top: 36px; background: var(--paper); }
  .card-front .brand { position: absolute; left: 10px; top: 30px; }
  .card-front .brand-dot { width: 14px; height: 14px; }
  .card-front .brand-name { font-size: 10px; }
  .card-person { position: absolute; left: 10px; top: 50px; font-size: 5px; font-weight: 700; color: var(--ink); }
  .card-person small { display: block; font-size: 4px; font-weight: 400; color: var(--muted); }
  .card-front .contact { position: absolute; left: 98px; top: 8px; font-size: 3.6px; line-height: 5.5px; }
  .card-front .footer-band { height: 5px; }
  .card-back { left: 948px; top: 36px; background: radial-gradient(ellipse at 50% 35%, var(--brand-light), var(--brand) 45%, var(--brand-dark)); display: flex; align-items: center; justify-content: center; }
  .card-back .brand-dot { background: #fff; width: 16px; height: 16px; }
  .card-back .brand-name { color: #fff; font-size: 10px; }

  /* Envelopes */
  .envelope-front { left: 780px; top: 148px; width: 408px; height: 176px; }
  .envelope-front .brand { position: absolute; left: 14px; top: 14px; }
  .envelope-front .contact { position: absolute; left: 14px; top: 38px; }
  .envelope-back { left: 780px; top: 352px; width: 408px; height: 180px; }
  .envelope-back svg { position: absolute; inset: 0; }
  .flap-mark { position: absolute; left: 50%; top: 22px; transform: translateX(-50%); width: 24px; height: 24px; border-radius: 50%; background: #fff; }
</style>
</head>
<body>

  <div class="item-label" style="left:19px;top:18px;width:281px">Fax Cover</div>
  <section class="sheet fax">
    <div class="brand"><span class="brand-dot"></span><span class="brand-name">QUORVALEN</span></div>
    <div class="contact">Tel: 555 014 2200<br>Fax: 555 014 2201<br>mdelaney@quorvalenconsulting.com<br>http://www.quorvalenconsutling.com</div>
    <div class="fax-title">FAX</div>
    <table class="fax-table">
      <tr><td>To:</td><td>From:</td></tr>
      <tr><td>Fax:</td><td>Pages:</td></tr>
      <tr><td>Phone:</td><td>Date:</td></tr>
      <tr><td>Re:</td><td>CC:</td></tr>
    </table>
    <div class="fax-options"><span>Urgent</span><span>For Review</span><span>Please Comment</span><span>Please Reply</span><span>Please Recycle</span></div>
    <div class="fax-divider"></div>
    <div class="ghost-circle" style="left:70px;top:340px;width:140px;height:140px"></div>
    <div class="footer-band"></div>
  </section>

  <div class="item-label" style="left:408px;top:18px;width:288px">Letterhead</div>
  <section class="sheet letterhead">
    <div class="brand"><span class="brand-dot"></span><span class="brand-name">QUORVALEN</span></div>
    <div class="contact">Tel: 555 014 2200<br>Fax: 555 014 2201<br>mdelaney@quorvalenconsulting.com<br>http://www.quorvalenconsutling.com</div>
    <div class="ghost-circle" style="left:74px;top:340px;width:140px;height:140px"></div>
    <div class="footer-band"></div>
  </section>

  <div class="item-label" style="left:780px;top:24px;width:156px">Business Card (Front)</div>
  <section class="card card-front">
    <div class="contact">Tel: 555 014 2200<br>Fax: 555 014 2201<br>48 Harrow Lane<br>mdelaney@quorvalenconsulting.com<br>http://www.quorvalenconsutling.com</div>
    <div class="brand"><span class="brand-dot"></span><span class="brand-name">QUORVALEN</span></div>
    <div class="card-person">Mark Delaney<small>System's Engineer</small></div>
    <div class="footer-band"></div>
  </section>

  <div class="item-label" style="left:948px;top:24px;width:156px">Business Card (Back)</div>
  <section class="card card-back">
    <div class="brand"><span class="brand-dot"></span><span class="brand-name">QUORVALEN</span></div>
  </section>

  <div class="item-label" style="left:780px;top:137px;width:408px">Envelope (Front)</div>
  <section class="sheet envelope-front">
    <div class="brand"><span class="brand-dot"></span><span class="brand-name">QUORVALEN</span></div>
    <div class="contact">48 Harrow Lane<br>http://www.quorvalenconsutling.com</div>
    <div class="ghost-circle" style="left:144px;top:40px;width:120px;height:120px"></div>
    <div class="footer-band"></div>
  </section>

  <div class="item-label" style="left:780px;top:341px;width:408px">Envelope (Back)</div>
  <section class="sheet envelope-back">
    <svg width="408" height="180" viewBox="0 0 408 180" aria-hidden="true">
      <defs>
        <linearGradient id="flap" x1="0" y1="0" x2="0" y2="1">
          <stop offset="0" stop-color="#0e2a5c"/>
          <stop offset="1" stop-color="#2a63b5"/>
        </linearGradient>
      </defs>
      <path d="M0 0 H408 V8 L204 78 L0 8 Z" fill="url(#flap)"/>
      <path d="M0 180 L204 90 L408 180" fill="none" stroke="#e2e4e8" stroke-width="1"/>
    </svg>
    <div class="flap-mark"></div>
  </section>

</body>
</html>
```